vorp business card design

vorp is an incubator within TRW Mediaworks focused on unlocking the potential in underserved niche micro-verticals on the web. our mission is to rapidly develop and foster emerging micro-verticals bc they are ripe for growth - building interesting and trusted content experiences with unqiue, useful and cutting-edge delivery methods.please do all copy (except for TRW Mediaworks, which must look as typed here and in logo) in all lowercase. Also please use spaces between phone # extensions not dashes or periods. I have attached all variations of the logo.
Industry/Entity Type
Business
Contact Information for Business Card
dale fenwright, ceo www.vorp.example 218 9th avenue 3rd floor oakland ca 94610 415 602 0002m 510 985 7966d dale.fenwright@vorp.example
Look and feel

```html
<!DOCTYPE html>
<html lang="en">
<head>
<meta charset="utf-8">
<title>vorp business card</title>
<link rel="stylesheet" href="https://fonts.googleapis.com/css2?family=Montserrat:wght@400;500&family=Source+Sans+3:wght@400&display=swap">
<style>
  :root {
    --backdrop: #e9e6e1;
    --card-frost: #f4f3f1;
    --card-edge: #d6d3ce;
    --ink: #1f1e1e;
    --band-dark: #1c1b1b;
    --teal: #1e7f78;
    --contact: #e6dcc2;
  }
  * { margin: 0; padding: 0; box-sizing: border-box; }
  html, body {
    width: 1200px; height: 1200px; overflow: hidden;
    background: var(--backdrop);
  }
  .canvas { position: relative; width: 1200px; height: 1200px; }
  .card {
    position: absolute; left: 100px; top: 305px;
    width: 1000px; height: 590px;
    border-radius: 22px; overflow: hidden;
    background: linear-gradient(160deg, #f9f8f6 0%, var(--card-frost) 60%, #ebe9e5 100%);
    box-shadow: 0 0 0 1px var(--card-edge), 0 18px 40px rgba(0,0,0,0.12);
  }
  .card-waves { position: absolute; inset: 0; width: 1000px; height: 590px; }
  .brand {
    position: absolute; left: 72px; top: 88px;
    display: flex; align-items: center; gap: 22px;
  }
  .brand-name {
    font-family: "Montserrat", sans-serif; font-weight: 500;
    font-size: 118px; line-height: 1; letter-spacing: -2px;
    color: var(--ink);
  }
  .brand-dot {
    width: 34px; height: 34px; border-radius: 50%;
    background: var(--teal); margin-top: 30px;
  }
  .tagline {
    position: absolute; left: 76px; top: 222px;
    font-family: "Montserrat", sans-serif; font-weight: 400;
    font-size: 23px; color: var(--ink);
  }
  .person-name {
    position: absolute; left: 76px; top: 322px;
    font-family: "Montserrat", sans-serif; font-weight: 500;
    font-size: 30px; color: var(--teal); letter-spacing: 0.3px;
  }
  .person-title {
    position: absolute; left: 78px; top: 368px;
    font-family: "Montserrat", sans-serif; font-weight: 400;
    font-size: 18px; color: var(--ink);
  }
  .contact-list {
    position: absolute; right: 46px; top: 382px;
    list-style: none;
    font-family: "Source Sans 3", sans-serif; font-size: 24px;
    color: var(--contact); text-align: right;
  }
  .contact-list li {
    height: 35px; line-height: 35px;
    display: flex; justify-content: flex-end; align-items: center; gap: 14px;
  }
  .contact-icon { width: 22px; height: 22px; flex: none; }
</style>
</head>
<body>
<div class="canvas">
  <div class="card">
    <svg class="card-waves" viewBox="0 0 1000 590" aria-hidden="true">
      <path class="dark-band" d="M0,535 C200,542 360,522 480,470 C650,380 820,260 1000,245 L1000,590 L0,590 Z" fill="var(--band-dark)"/>
      <path class="teal-ribbon" d="M1000,212 C820,226 650,338 480,440 C380,500 250,522 150,530 C260,538 380,518 480,470 C650,380 820,260 1000,245 Z" fill="var(--teal)"/>
      <path class="teal-crescent" d="M0,455 C120,492 260,520 430,522 C260,532 120,522 0,505 Z" fill="var(--teal)"/>
    </svg>

    <div class="brand">
      <span class="brand-name">vorp</span>
      <span class="brand-dot"></span>
    </div>
    <p class="tagline">a TRW Mediaworks incubator</p>

    <p class="person-name">Dale Fenwright</p>
    <p class="person-title">CEO</p>

    <ul class="contact-list">
      <li>www.vorp.example
        <svg class="contact-icon" viewBox="0 0 24 24"><path d="M4 9c0-3 3-5 8-5s8 2 8 5h-4l-1-2H9L8 9H4z M6 11h12l2 8H4z" fill="var(--teal)"/><circle cx="12" cy="15" r="2.2" fill="var(--band-dark)"/></svg>
      </li>
      <li>510 247 3318d
        <svg class="contact-icon" viewBox="0 0 24 24"><rect x="6" y="2" width="12" height="20" rx="2" fill="var(--teal)"/><rect x="8" y="5" width="8" height="12" fill="var(--band-dark)"/></svg>
      </li>
      <li>94610 415 738 1194m
        <svg class="contact-icon" viewBox="0 0 24 24"><rect x="2" y="5" width="20" height="14" rx="1.5" fill="var(--teal)"/><path d="M3 6l9 7 9-7" fill="none" stroke="var(--band-dark)" stroke-width="1.8"/></svg>
      </li>
      <li>dale.fenwright@vorp.example
        <svg class="contact-icon" viewBox="0 0 24 24"><circle cx="12" cy="12" r="10" fill="var(--teal)"/><g fill="none" stroke="var(--band-dark)" stroke-width="1.5"><ellipse cx="12" cy="12" rx="4.5" ry="10"/><path d="M2 12h20M4 7h16M4 17h16"/></g></svg>
      </li>
      <li>218 9th avenue 3rd floor oakland ca</li>
    </ul>
  </div>
</div>
</body>
</html>
```